Halcyon 88/3 (plot no. 9 sector 67 Noida)

We need a brochure designed for our upcoming premium office complex located in Delhi NCR. The brochure is meant to be circulated to potential tenants and property consultants.The brochure should showcase key aspects of the office complex, showcasing it as a premium "Grade A" building which has multiple energy conservation concepts. Since the building has been awarded a "ZELQ Platinum Pre-certification", this should be highlighted. The brochure should include location details, key project specifications, and renderings of the project facade. The brochure should also showcase the strength of the project developer, by giving some history of the developer's past projects. All relevant details to be included in the brochure are attached.

Target Market(s)

Potential customers and real estate brokers for leasing the office space

Industry/Entity Type

Real Estate

Font styles to use
Sans Serif

Colors

Designer to choose colors to be used in the design.

Requirements
Must have
• Cover page, location map, design detailing and brief description as per the attached documents
• Being a platinum rated Green Building, green aspects should be highlighted
Nice to have
• Bright colors and textured background
Should not have
• black must be avoided

```html
<!DOCTYPE html>
<html lang="en">
<head>
<meta charset="utf-8">
<title>Halcyon 88/3 Brochure</title>
<link href="https://fonts.googleapis.com/css2?family=Montserrat:wght@300;400;500;600;700&family=Lora:ital@1&display=swap" rel="stylesheet">
<style>
:root{
  --bg:#a9a9a9;
  --navy:#1d2f5e;
  --navy-deep:#15244b;
  --red:#c8323a;
  --white:#ffffff;
  --paper:#efefef;
  --ink:#2c3550;
  --muted:#6a7087;
  --soft:#c9cfe0;
  --teal:#3a86b5;
}
*{margin:0;padding:0;box-sizing:border-box}
html,body{width:747px;height:1200px;overflow:hidden}
body{background:var(--bg);font-family:'Montserrat',sans-serif;position:relative;color:var(--ink)}
.spread{position:absolute;left:24px;width:700px;height:253px;display:flex;box-shadow:0 8px 18px rgba(40,40,40,.35)}
.spread--covers{top:300px}
.spread--inside{top:640px}
.page{position:relative;width:350px;height:253px;overflow:hidden}
.brand{font-family:'Montserrat',sans-serif;font-weight:300;letter-spacing:3px;color:var(--white);white-space:nowrap}
.web-band{position:absolute;bottom:0;height:22px;background:var(--red);color:var(--white);font-family:'Lora',serif;font-style:italic;font-size:8px;display:flex;align-items:center;justify-content:center;letter-spacing:.5px;white-space:nowrap}

/* back cover */
.back{background:var(--navy-deep)}
.back__render{position:absolute;inset:0;background:linear-gradient(160deg,#2a3c6c 0%,#1b2a55 55%,#15244b 100%)}
.back__content{position:absolute;left:0;right:0;top:92px;text-align:center}
.back .brand{font-size:22px}
.back__heading{color:var(--red);font-size:7.5px;font-weight:600;margin-top:12px}
.back__rule{width:24px;height:1px;background:var(--red);margin:3px auto 5px}
.back__address{font-size:5.4px;line-height:7px;color:var(--white);font-weight:500}
.back__address p+p{margin-top:4px}
.back .web-band{left:125px;width:100px}

/* front cover */
.front__render{position:absolute;inset:0;background:linear-gradient(180deg,#4d7fc4 0%,#86aedc 30%,#c98a3e 55%,#d8b34a 72%,#5c6b3e 92%)}
.front .brand{position:absolute;left:18px;top:24px;font-size:21px}
.front .web-band{left:0;width:118px;bottom:8px;height:17px;justify-content:flex-start;padding-left:14px;font-size:7px}
.front__band{position:absolute;right:0;top:0;width:54px;height:253px;background:var(--navy)}
.front__title{position:absolute;right:27px;top:126px;transform:translate(50%,-50%) rotate(-90deg);white-space:nowrap;text-align:center;color:var(--white)}
.front__title .headline{font-weight:700;font-size:13px;letter-spacing:2px}
.front__title .sub{font-weight:400;font-size:5px;letter-spacing:2.5px;color:var(--soft);margin-top:3px}

/* inside left: location */
.location{background:var(--paper)}
.location__brand{position:absolute;left:6px;top:216px;transform:rotate(-90deg);transform-origin:left top;font-size:15px;color:var(--teal);font-weight:400;letter-spacing:2px;white-space:nowrap}
.location__map{position:absolute;left:64px;top:18px;width:269px;height:184px;background:linear-gradient(135deg,#8c8f78 0%,#a3a48c 40%,#7e8a6c 70%,#9a9a86 100%)}
.legend{position:absolute;left:124px;top:205px;display:grid;grid-template-columns:repeat(3,auto);column-gap:14px;row-gap:2px;font-size:4px;color:var(--muted)}
.legend span{display:flex;align-items:center;gap:3px;white-space:nowrap}
.legend i{display:inline-block;width:4px;height:4px}
.location .web-band{left:16px;width:126px;bottom:6px;height:17px;font-size:7px}

/* inside right: features */
.features{background:var(--white)}
.features__render{position:absolute;left:0;top:0;width:142px;height:253px;background:linear-gradient(180deg,#f2f2f2 0%,#c9c6c0 30%,#d98a2e 50%,#c9c6c0 75%,#7d8f6a 100%)}
.features__tab{position:absolute;left:120px;top:92px;width:22px;height:132px;background:var(--navy);border-radius:6px 0 0 6px;display:flex;align-items:center;justify-content:center}
.features__tab span{transform:rotate(-90deg);color:var(--white);font-weight:700;font-size:10px;letter-spacing:.5px;white-space:nowrap}
.features .brand{position:absolute;right:16px;top:14px;font-size:10px;color:var(--teal);font-weight:400;letter-spacing:1.5px}
.spec{position:absolute;left:155px;top:38px;width:180px;border-collapse:collapse;font-size:3.6px;line-height:4.4px}
.spec th{text-align:left;font-weight:600;color:var(--ink);width:58px;vertical-align:top;padding:1.6px 0}
.spec td{color:var(--muted);vertical-align:top;padding:1.6px 0}
.spec tr{border-top:.4px solid #dde0e6}
.features .web-band{right:16px;width:110px;bottom:6px;height:17px;font-size:7px}
</style>
</head>
<body>

<section class="spread spread--covers">
  <article class="page back">
    <div class="back__render" role="img" aria-label="Dimmed rendering of the office building facade under a navy overlay"></div>
    <div class="back__content">
      <div class="brand">HALCYON</div>
      <div class="back__heading">CONTACT US</div>
      <div class="back__rule"></div>
      <div class="back__address">
        <p>Site Office:<br>Plot No: GX-14 Sector 3,<br>Greater Noida(West)<br>Corporate Office:<br>C-21/4 Sector - 45, Noida 201303, India</p>
        <p>+91-9000011122, 0120-4000300</p>
        <p>halcyonone@infohalcyon.com</p>
      </div>
    </div>
    <div class="web-band">www.halcyonone.in</div>
  </article>

  <article class="page front">
    <div class="front__render" role="img" aria-label="Rendering of the office tower with orange and yellow facade fins against a blue sky"></div>
    <div class="brand">HALCYON</div>
    <div class="web-band">www.halcyonone.in</div>
    <div class="front__band"></div>
    <div class="front__title">
      <div class="headline">PREMIUM WORKSPACES</div>
      <div class="sub">GRADE A OFFICES</div>
    </div>
  </article>
</section>

<section class="spread spread--inside">
  <article class="page location">
    <div class="location__brand">HALCYON</div>
    <div class="location__map" role="img" aria-label="Aerial location map marking the project plots, nearby business parks and the expressway"></div>
    <div class="legend">
      <span><i style="background:#e8782f"></i>Halcyon 88/1</span>
      <span><i style="background:#2c5aa0"></i>Orion Business Park</span>
      <span><i style="background:#c8323a"></i>Noida - Greater Noida Expressway</span>
      <span><i style="background:#e8782f"></i>Halcyon 88/2</span>
      <span><i style="background:#2c5aa0"></i>City CNG Station</span>
      <span><i style="background:#3aa14a"></i>Noida Authority Park</span>
      <span><i style="background:#e8782f"></i>Halcyon 88/4</span>
      <span><i style="background:#2c5aa0"></i>Vela Systems</span>
      <span><i style="background:#c8323a;border-radius:50%"></i>Metro Station</span>
    </div>
    <div class="web-band">www.halcyonone.in</div>
  </article>

  <article class="page features">
    <div class="features__render" role="img" aria-label="Street-level rendering of the tower with its colourful facade and landscaped frontage"></div>
    <div class="features__tab"><span>FEATURES</span></div>
    <div class="brand">HALCYON</div>
    <table class="spec">
      <tr><th>Project Size</th><td>3,71,000 sq ft</td></tr>
      <tr><th>Project Land Area</th><td>2.5 Acres</td></tr>
      <tr><th>Number of Floors</th><td>Basement + Stilt + 11</td></tr>
      <tr><th>Typical Floor Size</th><td>1st - 10th Floor - 34,950 Sq. ft<br>11th Floor - 27,900 Sq. ft</td></tr>
      <tr><th>Sustainability</th><td>ZELQ Platinum Pre Certified (Energy savings in the range of 30-40% and water saving in the range of 20-30%)</td></tr>
      <tr><th>Efficiency</th><td>75%</td></tr>
      <tr><th>Parking</th><td>400 Cars expandable to 548</td></tr>
      <tr><th>Elevators</th><td>6 Dedicated Passenger Elevators of 16 Passenger Capacity each<br>2 Dedicated Service elevators of Capacity 1088 Kg each</td></tr>
      <tr><th>Earthquake Resistant Structure</th><td>Designed for Seismic Zone-IV</td></tr>
      <tr><th>Air Conditioning</th><td>Central Air Conditioning with N+1 configuration of Chillers with 24*7 Service</td></tr>
      <tr><th>Power Backup</th><td>100% power back up with N+1 redundancy</td></tr>
      <tr><th>Redundancy in rising main supply</th><td>Two separate rising mains for redundancy</td></tr>
      <tr><th>Ceiling Height</th><td>3.90 meters (floor to ceiling)</td></tr>
      <tr><th>Floor Loading</th><td>400 Kg/m2</td></tr>
      <tr><th>Building Management System</th><td>Building Management Systems infrastructure for the building with integration with HVAC systems will be provided</td></tr>
    </table>
    <div class="web-band">www.halcyonone.in</div>
  </article>
</section>

</body>
</html>
```